Looking for a creative label design for our retail coffee bags

We are a coffee manufacturer (coffee roaster) looking to re-brand our retail label for our coffee bags. Our main coffee blend that we sell is our Harborline Velvet Blend. You can use this name when creating the label. We are going for a look that represents our company as a coffee roaster. Please reference our website (www.brindlemugworks.com) and our Facebook page to learn more about our company and to give you more inspiration on creating this design.

Target Market(s)

Retail customers/grocery stores

Industry/Entity Type

Manufacturer

Requirements
Must have
• The size of the label has to be 3" width x 4" height

Logo must be Black
Nice to have
• We currently incorporate a color on our labels for each blend. For example, Harborline Velvet Blend (royal blue), Decaffeinated Blend (red), Breakfast Blend (green), Flavored coffees (gold).

Rustic/vintage style

```html
<!DOCTYPE html>
<html lang="en">
<head>
<meta charset="utf-8">
<title>Brindle Mugworks – Harborline Velvet Blend Label</title>
<link rel="stylesheet" href="https://fonts.googleapis.com/css2?family=Rye&family=Oswald:wght@500;600&family=Montserrat:wght@500&display=swap">
<style>
  :root {
    --page: #ffffff;
    --parchment-light: #efe9da;
    --parchment-mid: #e2d8c0;
    --parchment-edge: #cfc3a4;
    --leaf-tone: #d3cbb5;
    --ink: #1d1c1b;
    --badge: #2a2828;
    --gold: #b39a52;
    --royal: #1c2a8f;
    --royal-deep: #15216e;
    --torn-grey: #a9a496;
    --white: #ffffff;
  }
  html, body {
    margin: 0;
    width: 1200px;
    height: 800px;
    overflow: hidden;
    background: var(--page);
  }
  .label {
    position: absolute;
    left: 330px;
    top: 40px;
    width: 540px;
    height: 720px;
    display: block;
  }
  .label-paper { fill: url(#parchment); }
  .botanical-art { fill: var(--leaf-tone); opacity: 0.55; }
  .badge-tab, .badge-disc { fill: var(--badge); }
  .tab-rule { stroke: var(--gold); stroke-width: 1; }
  .badge-ring { fill: none; stroke: var(--white); stroke-width: 1; opacity: 0.85; }
  .brand-name {
    font-family: "Oswald", sans-serif;
    font-weight: 500;
    fill: var(--white);
    letter-spacing: 2px;
  }
  .origin-line {
    font-family: "Montserrat", sans-serif;
    font-weight: 500;
    font-size: 8.5px;
    letter-spacing: 2px;
    fill: var(--ink);
  }
  .title-rule { stroke: var(--ink); stroke-width: 2; }
  .blend-origin {
    font-family: "Oswald", sans-serif;
    font-weight: 600;
    font-size: 30px;
    fill: var(--ink);
  }
  .ornament { fill: var(--ink); opacity: 0.8; }
  .blend-feature {
    font-family: "Rye", serif;
    font-size: 92px;
    fill: var(--royal);
    stroke: var(--gold);
    stroke-width: 1;
    paint-order: stroke;
  }
  .blend-word {
    font-family: "Rye", serif;
    font-size: 74px;
    fill: var(--ink);
    stroke: var(--gold);
    stroke-width: 1;
    paint-order: stroke;
  }
  .roast-note {
    font-family: "Montserrat", sans-serif;
    font-weight: 500;
    font-size: 17px;
    letter-spacing: 4px;
    fill: var(--ink);
  }
  .torn-shadow { fill: var(--torn-grey); }
  .footer-band { fill: var(--royal); }
  .footer-texture { fill: var(--royal-deep); opacity: 0.6; }
  .footer-text {
    font-family: "Rye", serif;
    font-size: 16px;
    fill: var(--white);
  }
</style>
</head>
<body>
<svg class="label" viewBox="0 0 540 720" xmlns="http://www.w3.org/2000/svg">
  <defs>
    <radialGradient id="parchment" cx="50%" cy="45%" r="75%">
      <stop offset="0%" stop-color="var(--parchment-light)"/>
      <stop offset="70%" stop-color="var(--parchment-mid)"/>
      <stop offset="100%" stop-color="var(--parchment-edge)"/>
    </radialGradient>
    <path id="origin-arc" d="M 125 171 A 143 143 0 0 0 411 171"/>
  </defs>

  <rect class="label-paper" x="0" y="0" width="540" height="720"/>

  <g role="img" aria-label="Faint engraved coffee branch with leaves and cherries">
    <ellipse class="botanical-art" cx="95" cy="230" rx="95" ry="110"/>
    <ellipse class="botanical-art" cx="455" cy="240" rx="90" ry="130"/>
  </g>

  <rect class="badge-tab" x="216" y="0" width="103" height="100"/>
  <line class="tab-rule" x1="226" y1="0" x2="226" y2="48"/>
  <line class="tab-rule" x1="309" y1="0" x2="309" y2="48"/>
  <circle class="badge-disc" cx="268" cy="171" r="128"/>
  <circle class="badge-ring" cx="268" cy="171" r="116"/>
  <text class="brand-name" x="268" y="166" text-anchor="middle" font-size="38">BRINDLE</text>
  <text class="brand-name" x="268" y="202" text-anchor="middle" font-size="26">MUGWORKS</text>

  <text class="origin-line">
    <textPath href="#origin-arc" startOffset="50%" text-anchor="middle">PROUDLY ROASTED IN ALDER FALLS, OH SINCE 1994.</textPath>
  </text>

  <line class="title-rule" x1="127" y1="331" x2="462" y2="331"/>
  <text class="blend-origin" x="130" y="363" textLength="160" lengthAdjust="spacingAndGlyphs">HARBORLINE</text>
  <g role="img" aria-label="Vintage scroll flourish">
    <rect class="ornament" x="300" y="343" width="162" height="14" rx="7"/>
  </g>
  <line class="title-rule" x1="127" y1="369" x2="462" y2="369"/>

  <text class="blend-feature" x="268" y="458" text-anchor="middle" textLength="400" lengthAdjust="spacingAndGlyphs">VELVET</text>
  <text class="blend-word" x="264" y="530" text-anchor="middle" textLength="240" lengthAdjust="spacingAndGlyphs">BLEND</text>

  <g role="img" aria-label="Vintage divider flourish">
    <rect class="ornament" x="154" y="549" width="228" height="8" rx="4"/>
  </g>
  <g role="img" aria-label="Row of five coffee beans marking roast strength">
    <rect class="ornament" x="216" y="579" width="102" height="18" rx="9"/>
  </g>

  <text class="roast-note" x="264" y="625" text-anchor="middle" textLength="256">FRESHLY ROASTED</text>

  <path class="torn-shadow" d="M0 638 L30 634 L60 640 L95 632 L130 639 L170 633 L205 641 L240 635 L280 640 L320 632 L360 639 L400 634 L440 641 L480 636 L515 640 L540 635 L540 660 L0 660 Z"/>
  <path class="footer-band" d="M0 652 L35 646 L70 653 L110 645 L150 652 L190 647 L230 654 L270 646 L310 653 L350 645 L390 652 L430 647 L470 654 L505 646 L540 650 L540 720 L0 720 Z"/>
  <g role="img" aria-label="Subtle coffee bean pattern on blue band">
    <rect class="footer-texture" x="0" y="660" width="540" height="60"/>
  </g>
  <text class="footer-text" x="264" y="677" text-anchor="middle">NET WT. 16OZ</text>
  <text class="footer-text" x="264" y="700" text-anchor="middle" textLength="232" lengthAdjust="spacingAndGlyphs">WWW.BRINDLEMUGWORKS.COM</text>
</svg>
</body>
</html>
```